Verostel business card

Business card for sustainable investment company called "Verostel". Verostel is an exchange platform selling carbon credits between buyers and sellers. Carbon Credits are an environmental commodity for reducing global carbon emissions.

the card should obviously have our logo and the theme should be sustainability/environment mixed with a trading platform.

Contact Information for Business Card

Logo, Name, Title, Phone, Email

Colors
0054AA
0677BA
7BADD7
CADEEF
E8F1F8
0094D4
00A9DD
6FCCEA
C7EBF8
E9F6FB
00AB8E
00BBA5
67D7C9
C6EFE9
E9F9F6
59FF00
82FF00
B8FF75
E3FFCB
F4FFEA

```html
<!DOCTYPE html>
<html lang="en">
<head>
<meta charset="utf-8">
<title>Verostel business card</title>
<link rel="stylesheet" href="https://fonts.googleapis.com/css2?family=Montserrat:wght@400;600;700&display=swap">
<style>
  :root {
    --page: #ffffff;
    --navy: #172b52;
    --ink: #555555;
    --rule: #8a8a8a;
    --frame: #8c8c8c;
    --mark: #3f86c6;
    --mark-faint: #5e6f8a;
    --white: #ffffff;
  }
  * { margin: 0; padding: 0; box-sizing: border-box; }
  html, body {
    width: 1200px; height: 900px; overflow: hidden;
    background: var(--page);
    font-family: "Montserrat", Arial, sans-serif;
  }
  .canvas { position: relative; width: 1200px; height: 900px; }
  .card {
    position: absolute; top: 303px; width: 475px; height: 299px; overflow: hidden;
  }
  .card--front { left: 116px; background: var(--white); border: 1px solid var(--frame); }
  .card--back { left: 616px; background: var(--navy); }

  .brand { position: absolute; display: flex; align-items: center; }
  .brand__dot { border-radius: 50%; background: var(--mark); flex: none; }
  .brand__name { font-weight: 700; letter-spacing: 0.04em; line-height: 1; }

  .card--front .brand { left: 168px; top: 31px; }
  .card--front .brand__dot { width: 52px; height: 52px; margin-right: 33px; }
  .card--front .brand__name { font-size: 37px; color: var(--navy); }

  .card--back .brand { left: 200px; top: 223px; }
  .card--back .brand__dot { width: 44px; height: 44px; margin-right: 30px; }
  .card--back .brand__name { font-size: 31px; color: var(--white); }

  .back-accent {
    position: absolute; left: -70px; top: 176px;
    width: 230px; height: 230px; border-radius: 50%;
    background: var(--mark-faint);
  }

  .contact {
    position: absolute; left: 32px; top: 100px; height: 173px;
    border-left: 1px solid var(--rule); padding-left: 6px; color: var(--ink);
  }
  .contact__name {
    position: absolute; left: 6px; top: 33px; white-space: nowrap;
    font-weight: 700; font-size: 14px; letter-spacing: 0.02em;
  }
  .contact__title {
    position: absolute; left: 6px; top: 54px; white-space: nowrap;
    font-size: 11px; letter-spacing: 0.02em;
  }
  .contact__address {
    position: absolute; left: 6px; top: 71px; white-space: nowrap;
    font-size: 13px; line-height: 13px; letter-spacing: 0.01em;
  }
  .contact__line {
    position: absolute; left: 6px; white-space: nowrap;
    font-size: 13px; display: flex; align-items: center; gap: 4px;
  }
  .contact__line--phone { top: 104px; }
  .contact__line--email { top: 124px; }
  .contact__icon { width: 13px; height: 11px; fill: var(--ink); flex: none; }
</style>
</head>
<body>
<main class="canvas">
  <section class="card card--front">
    <div class="brand">
      <span class="brand__dot"></span>
      <span class="brand__name">VEROSTEL</span>
    </div>
    <div class="contact">
      <p class="contact__name">MARLOW KESSING</p>
      <p class="contact__title">Managing Director</p>
      <p class="contact__address">48 Alder Crest Way<br>Fairhaven,</p>
      <p class="contact__line contact__line--phone">
        <svg class="contact__icon" viewBox="0 0 13 11" aria-hidden="true">
          <path d="M0 3.2C0 1.2 3 0 6.5 0S13 1.2 13 3.2v.8h-3.2V2.8H3.2V4H0z"/>
          <path d="M2.2 5.2 4 3.4h5l1.8 1.8V11H2.2z"/>
          <circle cx="6.5" cy="7.3" r="1.6" fill="#fff"/>
        </svg>
        555-214-0387
      </p>
      <p class="contact__line contact__line--email">
        <svg class="contact__icon" viewBox="0 0 13 11" aria-hidden="true">
          <path d="M0 1h13v9H0z"/>
          <path d="M.6 1.6 6.5 6.2l5.9-4.6M.6 9.4l4.3-4.1m7.5 4.1L8.1 5.3" stroke="#fff" stroke-width="0.8" fill="none"/>
        </svg>
        marlow@kessingworks.com
      </p>
    </div>
  </section>

  <section class="card card--back">
    <span class="back-accent"></span>
    <div class="brand">
      <span class="brand__dot"></span>
      <span class="brand__name">VEROSTEL</span>
    </div>
  </section>
</main>
</body>
</html>
```